Buch-/E-Book-Cover für Ratgeber gesucht
Zielgruppe
Es handelt sich um einen Ratgeber zum Thema 'Die Brücke zur Ruhe: Wie du es nun lernst, gelassen zu leben!'.
Das Buch richtet sich vor allem an Frauen im Alter zwischen 18-45 Jahren.
Wie der Titel des Buches bereits aussagt, besteht das Buch aus verschiedenen Kapiteln zum Thema: 'Wie man glücklich wird'.
Aufgabenstellung
*UPDATE: 16.02.2023 / 19:00 Uhr*
Ich habe Beispielcover (1-7) hochgeladen, die ihr als Inspiration für eure Covervorschläge nutzen könnt. Es sollten natürlich keine 1:1 Kopien sein.
Danke!
1.) Der Haupttitel des Buches lautet 'Die Brücke zur Ruhe'
2.) Der Untertitel des Buches lautet 'Wie du es nun lernst, gelassen zu leben!'
3.) Der Name der Autorin lautet 'Lina Hartung'
4.) Der Verlagsname lautet 'deine Morgenstille'.
5.)Das Cover sollte eine Mischung aus 'modern/schlicht' und 'klassisch' sein und nach Möglichkeit Elemente enthalten wie:
- der Hintergrund aus einer Pastellfarbe. Wichtige Elemente können jedoch mit einer Kontrastfarbe hervorgehoben werden
- kein 'eintöniger/einfarbiger' Hintergrund, sondern z. B. mit einem 'Muster'
- Der Haupttitel kann gerne aus verschiedenen Schriftarten bestehen (modern/klassisch) und etwas größer sein, damit er direkt ersichtlich ist.
- aussagekräftige(s) Symbol(e) passend zum Titel ('Die Brücke zur Ruhe').
- Vektorgrafiken/-elemente anstelle von 'Fotos'
6.) Es wird ein Cover für ein Ebook, Taschenbuch als auch Hardcover benötigt.
7.) Das Buch hat ca. 229 Seiten und ein Format von 6x9 Zoll. Die Formatvorlage für Bücherhafen und andere Plattformen kann gerne zu Verfügung gestellt werden.
8.) Ich besitze eine kostenpflichtige Lizenz bei bildmarkt, sodass hier gerne jede Grafik bezogen werden kann. Wenn eine Grafik nur auf einer anderen Plattform vorhanden ist, dann bin ich bereit diese zu kaufen.
9.) Es werden weitere Bücher in dem Themengebiet folgen, sodass eine langfristige Kooperation zum Designen von Covern angedacht ist.

```html
<!DOCTYPE html>
<html lang="de">
<head>
<meta charset="utf-8">
<title>Die Brücke zur Ruhe – Lina Hartung</title>
<link rel="stylesheet" href="https://fonts.googleapis.com/css2?family=Caveat+Brush&family=Sacramento&family=Permanent+Marker&family=Montserrat:wght@500&display=swap">
<style>
  :root {
    --ink: #6a3a1e;
    --tag: #7a4528;
    --tag-text: #f6e6d2;
    --cream: #faeede;
    --peach: #f7dcc4;
    --rose: #f2cfd3;
    --lilac: #d9d4ea;
    --sky: #cfe0ea;
    --key: #3a3431;
    --twine: #c98a4c;
  }
  * { margin: 0; padding: 0; box-sizing: border-box; }
  html, body { width: 800px; height: 1200px; overflow: hidden; background: #ffffff; }
  .cover {
    position: relative;
    width: 800px;
    height: 1200px;
    overflow: hidden;
    background:
      radial-gradient(ellipse 60% 40% at 95% 90%, var(--sky), transparent 70%),
      radial-gradient(ellipse 55% 45% at 90% 55%, var(--lilac), transparent 70%),
      radial-gradient(ellipse 60% 45% at 85% 10%, var(--rose), transparent 70%),
      radial-gradient(ellipse 50% 35% at 5% 95%, var(--peach), transparent 70%),
      linear-gradient(160deg, var(--cream) 0%, #f9e8e2 55%, #f1dde4 100%);
    color: var(--ink);
  }
  .title { position: absolute; left: 0; right: 0; top: 40px; text-align: center; }
  .title__script {
    display: block;
    font-family: "Sacramento", cursive;
    font-size: 130px;
    line-height: 1;
    height: 100px;
  }
  .title__script--first { margin-left: -20px; }
  .title__script--second { margin-top: 4px; height: 110px; font-size: 150px; margin-left: 30px; }
  .title__caps {
    display: block;
    font-family: "Caveat Brush", sans-serif;
    font-size: 118px;
    line-height: 1;
    letter-spacing: 1px;
    margin-top: 6px;
  }
  .title__main {
    display: block;
    font-family: "Caveat Brush", sans-serif;
    font-size: 270px;
    line-height: 0.85;
    letter-spacing: 4px;
    margin-top: 14px;
  }
  .key-photo {
    position: absolute;
    left: 68px;
    top: 660px;
    width: 300px;
    height: 412px;
  }
  .author-tag {
    position: absolute;
    left: 392px;
    top: 655px;
    width: 290px;
    height: 128px;
    background: var(--tag);
    transform: rotate(13deg);
    clip-path: polygon(12% 0, 100% 0, 100% 100%, 12% 100%, 0 50%);
    display: flex;
    align-items: center;
    justify-content: center;
    padding-left: 30px;
  }
  .author-tag__name {
    font-family: "Permanent Marker", sans-serif;
    font-size: 30px;
    color: var(--tag-text);
    letter-spacing: 1px;
  }
  .subtitle {
    position: absolute;
    left: 330px;
    top: 922px;
    width: 400px;
    text-align: center;
    font-family: "Permanent Marker", sans-serif;
    font-size: 29px;
    line-height: 1.35;
  }
  .publisher {
    position: absolute;
    left: 0;
    right: 0;
    top: 1126px;
    text-align: center;
    font-family: "Montserrat", sans-serif;
    font-weight: 500;
    font-size: 22px;
    letter-spacing: 2px;
    color: #2e241f;
  }
</style>
</head>
<body>
  <main class="cover">
    <h1 class="title">
      <span class="title__script title__script--first">Die</span>
      <span class="title__caps">BRÜCKE</span>
      <span class="title__script title__script--second">zur</span>
      <span class="title__main">RUHE</span>
    </h1>

    <svg class="key-photo" viewBox="0 0 300 412" role="img" aria-label="Foto eines alten schwarzen Schlüssels mit Juteschnur, schräg liegend">
      <defs>
        <linearGradient id="keyArea" x1="0" y1="0" x2="1" y2="1">
          <stop offset="0" stop-color="#e9d6c4" stop-opacity="0"/>
          <stop offset="0.5" stop-color="#b99a84" stop-opacity="0.35"/>
          <stop offset="1" stop-color="#e9d6c4" stop-opacity="0"/>
        </linearGradient>
      </defs>
      <rect width="300" height="412" rx="30" fill="url(#keyArea)"/>
    </svg>

    <div class="author-tag">
      <span class="author-tag__name">LINA HARTUNG</span>
    </div>

    <p class="subtitle">WIE DU ES NUN LERNST<br>GELASSEN ZU LEBEN!</p>

    <p class="publisher">DeineMorgenstille</p>
  </main>
</body>
</html>
```